Label Design for Nuts package*

Develop the design for a label for nuts sold in a paperbag.

you can find our website here: www.kornfeld-snack.de.
Here comes the link to our catalogue: https://www.blattwerk-docs.com/de/document/read/48172956/kornfeld-premium-snacks-gesamtkatalog-2019

With this product we are targeting private customers who want to buy nuts with plastic free packaging online.
The colours of the label should fit the brown paper bag.

```html
<!DOCTYPE html>
<html lang="de">
<head>
<meta charset="utf-8">
<title>Kornfeld – Schatzsucher Etikett</title>
<link rel="stylesheet" href="https://fonts.googleapis.com/css2?family=Nunito:wght@300;600;700&family=Open+Sans:wght@700&family=Libre+Baskerville&display=swap">
<style>
  :root {
    --kraft: #d8c4a8;
    --navy: #0f1522;
    --copper: #c49a7a;
    --title: #c79a78;
    --brand: #8a4a3a;
    --cream: #e8d8c0;
    --tagline: #c8a890;
    --ring: #a69a88;
    --rule: #8a7560;
  }
  html, body {
    margin: 0;
    padding: 0;
    width: 1090px;
    height: 1200px;
    overflow: hidden;
    background: var(--kraft);
  }
  .label {
    position: relative;
    width: 1090px;
    height: 1200px;
    overflow: hidden;
  }
  .label__art {
    position: absolute;
    inset: 0;
  }
  .brand {
    position: absolute;
    top: 168px;
    left: 212px;
    width: 668px;
    display: flex;
    align-items: center;
    justify-content: center;
    gap: 16px;
  }
  .brand__dot {
    width: 26px;
    height: 26px;
    border-radius: 50%;
    background: var(--brand);
  }
  .brand__name {
    font-family: "Nunito", sans-serif;
    font-weight: 300;
    font-size: 68px;
    line-height: 1;
    letter-spacing: 4px;
    color: var(--brand);
  }
  .tagline {
    position: absolute;
    top: 258px;
    left: 212px;
    width: 668px;
    text-align: center;
    font-family: "Libre Baskerville", serif;
    font-size: 22px;
    letter-spacing: 5px;
    color: var(--tagline);
  }
  .product-name {
    position: absolute;
    top: 382px;
    left: 180px;
    width: 730px;
    text-align: center;
    font-family: "Open Sans", sans-serif;
    font-weight: 700;
    font-size: 80px;
    line-height: 1.2;
    color: var(--title);
  }
  .description {
    position: absolute;
    top: 552px;
    left: 212px;
    width: 668px;
    text-align: center;
    font-family: "Nunito", sans-serif;
    font-weight: 600;
    font-size: 38px;
    line-height: 51px;
    color: var(--cream);
  }
  .weight {
    position: absolute;
    top: 1134px;
    left: 445px;
    width: 200px;
    text-align: center;
    font-family: "Nunito", sans-serif;
    font-weight: 700;
    font-size: 32px;
    color: #ffffff;
  }
</style>
</head>
<body>
  <main class="label">
    <svg class="label__art" width="1090" height="1200" viewBox="0 0 1090 1200">
      <defs>
        <radialGradient id="nut-tones" cx="50%" cy="70%" r="70%">
          <stop offset="0" stop-color="#c98a55"/>
          <stop offset="0.55" stop-color="#a86538"/>
          <stop offset="1" stop-color="#7a4526"/>
        </radialGradient>
      </defs>
      <rect class="side-panel" x="0" y="0" width="1090" height="1200" fill="var(--kraft)"/>
      <rect class="side-stripe" x="193" y="0" width="7" height="1200" fill="var(--copper)"/>
      <rect class="side-stripe" x="886" y="0" width="7" height="1200" fill="var(--copper)"/>
      <rect class="center-band" x="212" y="0" width="668" height="1200" fill="var(--navy)"/>
      <line class="tagline-rule" x1="408" y1="296" x2="684" y2="296" stroke="var(--brand)" stroke-width="1.5"/>
      <circle class="tagline-rule-dot" cx="545" cy="296" r="4" fill="none" stroke="var(--brand)" stroke-width="1.5"/>
      <line class="description-rule" x1="286" y1="538" x2="791" y2="538" stroke="var(--rule)" stroke-width="1.5"/>
      <line class="description-rule" x1="286" y1="666" x2="791" y2="666" stroke="var(--rule)" stroke-width="1.5"/>
      <circle class="window-ring" cx="545" cy="1206" r="476" fill="var(--ring)"/>
      <circle class="product-photo" cx="545" cy="1206" r="456" fill="url(#nut-tones)" role="img" aria-label="Foto einer Nussmischung mit Cashewkernen, Mandeln, Haselnüssen, Walnüssen und Pistazien"/>
      <circle class="weight-badge" cx="545" cy="1203" r="94" fill="var(--navy)"/>
    </svg>

    <div class="brand">
      <span class="brand__dot"></span>
      <span class="brand__name">kornfeld</span>
    </div>
    <div class="tagline">PREMIUM SNACKS</div>
    <h1 class="product-name" style="margin:0">SCHATZSUCHER</h1>
    <p class="description" style="margin:0">ofengeröstete<br>cashewkerne mit curry</p>
    <div class="weight">250gm</div>
  </main>
</body>
</html>
```